Business card design needed

Mechanical services (heavy)
Training needs
Air conditioning (Automotive)
Parts Supplier

Industry/Entity Type

Automotive

Contact Information for Business Card

R T Mechanical Services
Colin Harwood (director)
47 Marlow Ridge highway
North Kelbrook W.A 6218
Mobile: 0417 563 904
rtmechanical4@mailvex.com

```html
<!DOCTYPE html>
<html lang="en">
<head>
<meta charset="utf-8">
<title>R T Mechanical – Business Card</title>
<link rel="stylesheet" href="https://fonts.googleapis.com/css2?family=Ubuntu:wght@300;400;500&display=swap">
<style>
  :root {
    --page-bg: #e4e5e8;
    --navy-deep: #0f1322;
    --navy-mid: #1b2036;
    --ink: #1d1f26;
    --ink-soft: #4a4d57;
    --paper: #ffffff;
    --brand-red: #d9343b;
    --brand-blue: #2a62b8;
    --faint-red: #f3d6d7;
    --card-w: 560px;
    --card-h: 320px;
  }
  * { box-sizing: border-box; margin: 0; padding: 0; }
  html, body {
    width: 1200px; height: 900px; overflow: hidden;
    background: var(--page-bg);
    font-family: "Ubuntu", sans-serif;
  }
  .sheet {
    width: 1200px; height: 900px;
    display: flex; flex-direction: column;
    align-items: center; justify-content: center; gap: 60px;
  }
  .card {
    position: relative;
    width: var(--card-w); height: var(--card-h);
    border-radius: 4px; overflow: hidden;
    box-shadow: 0 10px 28px rgba(0,0,0,.18);
  }

  /* Back side */
  .card--back {
    background: radial-gradient(circle at 80% 20%, var(--navy-mid), var(--navy-deep) 70%);
    color: #e9ecf3;
  }
  .back-deco {
    position: absolute; right: -70px; top: -60px;
    width: 330px; height: 330px; border-radius: 50%;
    background: rgba(255,255,255,.04);
  }
  .services {
    position: absolute; left: 40px; top: 34px;
    list-style: none; font-size: 14px; font-weight: 300; line-height: 1.45;
  }
  .services li::before { content: "• "; }
  .brand {
    position: absolute; display: flex; align-items: center; gap: 14px;
  }
  .card--back .brand { left: 40px; bottom: 58px; }
  .brand-dot {
    width: 54px; height: 54px; border-radius: 50%;
    background: var(--brand-blue);
  }
  .brand-name { font-size: 26px; font-weight: 500; letter-spacing: -.2px; }

  /* Front side */
  .card--front { background: var(--paper); color: var(--ink); }
  .front-deco {
    position: absolute; right: -60px; bottom: -150px;
    width: 320px; height: 320px; border-radius: 50%;
    background: var(--faint-red); opacity: .6;
  }
  .card--front .brand { left: 40px; top: 30px; }
  .card--front .brand-dot { background: var(--brand-red); }
  .card--front .brand-name { color: var(--ink); }
  .person { position: absolute; left: 40px; top: 116px; }
  .person-name { font-size: 20px; font-weight: 400; }
  .person-role { font-size: 12px; font-weight: 300; color: var(--ink-soft); margin-top: 2px; }
  .contacts { list-style: none; margin-top: 16px; font-size: 13px; font-weight: 300; }
  .contacts li { display: flex; align-items: center; gap: 8px; line-height: 1.7; }
  .contacts svg { width: 12px; height: 12px; fill: var(--ink); }
  .address {
    position: absolute; right: 40px; bottom: 36px;
    font-size: 14px; font-weight: 300; line-height: 1.45; text-align: left;
    font-style: normal;
  }
</style>
</head>
<body>
<main class="sheet">

  <section class="card card--back" aria-label="Card back">
    <div class="back-deco"></div>
    <ul class="services">
      <li>Mechanical services (heavy)</li>
      <li>Training needs</li>
      <li>Air conditioning (Automotive)</li>
      <li>Parts Supplier</li>
    </ul>
    <div class="brand">
      <span class="brand-dot"></span>
      <span class="brand-name">R T Mechanical</span>
    </div>
  </section>

  <section class="card card--front" aria-label="Card front">
    <div class="front-deco"></div>
    <div class="brand">
      <span class="brand-dot"></span>
      <span class="brand-name">R T Mechanical</span>
    </div>
    <div class="person">
      <p class="person-name">Colin Harwood</p>
      <p class="person-role">director</p>
      <ul class="contacts">
        <li>
          <svg viewBox="0 0 12 12" aria-hidden="true"><path d="M3 0h6a1 1 0 0 1 1 1v10a1 1 0 0 1-1 1H3a1 1 0 0 1-1-1V1a1 1 0 0 1 1-1zm0 1.5v8h6v-8z"/></svg>
          0417 563 904
        </li>
        <li>
          <svg viewBox="0 0 12 12" aria-hidden="true"><path d="M0 2h12v8H0zm1 1v.3l5 3.2 5-3.2V3z"/></svg>
          rtmechanical4@mailvex.com
        </li>
      </ul>
    </div>
    <address class="address">
      47 Marlow Ridge highway<br>
      North Kelbrook W.A 6218
    </address>
  </section>

</main>
</body>
</html>
```